Does Faith Need Walls? Does Faith Need Us?

I would like to see what your designers can come up with for a Book cover design. It is a book about church, which addresses the long-standing question: is the church people/a group of people, or is it a building/organization?
This is my fourth book on Christian life and teachings, and will include the contents of several newsletters I've written and distributed over the years.
Finished size would be 5.5 inches wide x 8.5 inches tall.
I have attached the basic artwork from a newsletter so it would be ideal to have these included in the design.
However, the type and font is not very dynamic.
I would like to have someone try using either silhouettes of people and a building, contrasting the two - as long as it doesn’t look like a cartoon.
The idea being is the church a building, or is it people?

The title of the book is:
Does Faith Need Walls?
Does Faith Need Us?

Subhead:

'Around One Humble Table Together’: How True Kinship & Devotion Grow Strong

By Lionel Pettigrew

```html
<!DOCTYPE html>
<html lang="en">
<head>
<meta charset="utf-8">
<title>Does Faith Need Walls? Does Faith Need Us? — Book Cover</title>
<link href="https://fonts.googleapis.com/css2?family=Bebas+Neue&display=swap" rel="stylesheet">
<style>
  :root {
    --page-bg: #e4e4e4;
    --cover-dark: #3a2718;
    --cover-mid: #5e4128;
    --ground-light: #c9a87a;
    --glow-core: #fff8e4;
    --title-white: #f7f7f7;
    --title-blue: #17a9e6;
    --author-grey: #ddd8d2;
  }
  * { margin: 0; padding: 0; box-sizing: border-box; }
  html, body {
    width: 1200px;
    height: 900px;
    overflow: hidden;
    background: var(--page-bg);
  }
  .stage {
    width: 1200px;
    height: 900px;
    display: flex;
    align-items: center;
    justify-content: center;
  }
  .book-cover {
    position: relative;
    width: 439px;
    height: 658px;
    overflow: hidden;
    font-family: "Bebas Neue", "Arial Narrow", sans-serif;
  }
  .cover-art {
    position: absolute;
    inset: 0;
    background:
      radial-gradient(ellipse 12% 30% at 50% 60%, var(--glow-core) 0%, rgba(255,238,196,0.85) 45%, rgba(243,217,160,0) 100%),
      radial-gradient(ellipse 55% 30% at 50% 95%, var(--ground-light) 0%, rgba(160,120,76,0.5) 50%, rgba(90,60,35,0) 100%),
      radial-gradient(ellipse 70% 60% at 50% 55%, var(--cover-mid) 0%, var(--cover-dark) 100%);
  }
  .cover-line {
    position: absolute;
    left: 0;
    right: 0;
    text-align: center;
    line-height: 0.7;
    white-space: nowrap;
  }
  .title-lead {
    color: var(--title-white);
    font-size: 60px;
  }
  .title-key {
    color: var(--title-blue);
    font-size: 118px;
  }
  .lead-one { top: 44px; }
  .key-one { top: 98px; }
  .lead-two { top: 196px; }
  .key-two { top: 254px; }
  .subtitle {
    position: absolute;
    left: 0;
    right: 0;
    top: 356px;
    text-align: center;
    color: var(--title-white);
    font-size: 19px;
    line-height: 24px;
    text-shadow: 0 1px 3px rgba(60,40,20,0.6);
  }
  .author {
    position: absolute;
    left: 0;
    right: 0;
    top: 616px;
    text-align: center;
    color: var(--author-grey);
    font-size: 30px;
    line-height: 0.7;
    text-shadow: 0 1px 4px rgba(60,40,20,0.7);
  }
</style>
</head>
<body>
  <main class="stage">
    <article class="book-cover">
      <div class="cover-art" role="img" aria-label="Photograph contrasting a massive dark stone church wall, pierced by a glowing cross-shaped doorway, with a small group of people in silhouette walking together along the lit path toward the light"></div>
      <h1 class="title">
        <span class="cover-line title-lead lead-one">DOES FAITH NEED</span>
        <span class="cover-line title-key key-one">WALLS?</span>
        <span class="cover-line title-lead lead-two">DOES FAITH NEED</span>
        <span class="cover-line title-key key-two">US?</span>
      </h1>
      <p class="subtitle">'AROUND ONE HUMBLE TABLE TOGETHER’:<br>HOW TRUE KINSHIP &amp; DEVOTION GROW STRONG</p>
      <p class="author">BY LIONEL PETTIGREW</p>
    </article>
  </main>
</body>
</html>
```